BrightPine Real Estate Sign

We are in the process of rebranding our business and need a new For Sale \ Sold sign.
We're a prestige real estate agency and therefore require a really stylish sign.
I've uploaded the following files
1. The new company logo
2. "sample sign.jpg" which shows the type of sign we would like. It is a metal sign with a top panel and bottom panel.
3. Our previous sign "previous sign.jpg" if you're interested in seeing it.
The sign must be black with white text.
Our thoughts are that the top panel (refer to sample sign) would contain the text "For Sale" or "Sold". These would be two separate panels which are interchangeable and could be screwed in place.
The bottom panel would not contain any photos like the sample. However, it may contain our logo and my contact details etc.
The sign is 900mm wide x 1200mm high.
My details are:
Name: Gareth Wimble
Web: www.bprealestate.com.au
Email: sales@bprealestate.com.au
Phone: 0491 650 387

```html
<!DOCTYPE html>
<html lang="en">
<head>
<meta charset="utf-8">
<title>BrightPine Real Estate – Sold / For Sale Signs</title>
<link rel="stylesheet" href="https://fonts.googleapis.com/css2?family=Nunito:wght@800&family=Tinos:wght@700&display=swap">
<style>
  :root {
    --sign-black: #000000;
    --sign-white: #ffffff;
    --footer-ink: #000000;
    --gap: 6px;
  }
  * { margin: 0; padding: 0; box-sizing: border-box; }
  html, body {
    width: 1200px;
    height: 797px;
    overflow: hidden;
    background: var(--sign-white);
  }
  .sign-set {
    position: relative;
    width: 1200px;
    height: 797px;
    display: flex;
    gap: var(--gap);
    background: var(--sign-white);
  }
  .sign {
    position: relative;
    width: 597px;
    height: 797px;
  }
  .sign__panel {
    position: absolute;
    left: 0; top: 0;
    width: 597px;
    height: 720px;
    background: var(--sign-black);
    color: var(--sign-white);
    font-family: "Nunito", "Arial Rounded MT Bold", sans-serif;
    font-weight: 800;
    text-align: center;
  }
  .sign__headline {
    position: absolute;
    left: 0; right: 0;
    font-size: 158px;
    letter-spacing: 3px;
    font-weight: 800;
  }
  .sign--sold .sign__headline { top: 140px; line-height: 158px; }
  .sign--sale .sign__headline { top: 23px; line-height: 183px; }

  .brand {
    position: absolute;
    left: 0; right: 0;
    top: 608px;
    height: 60px;
    display: flex;
    align-items: center;
    justify-content: center;
    gap: 16px;
  }
  .brand__mark {
    width: 58px;
    height: 58px;
    background: var(--sign-white);
    flex: none;
  }
  .brand__name {
    font-family: "Nunito", "Arial Rounded MT Bold", sans-serif;
    font-weight: 800;
    font-size: 31px;
    line-height: 40px;
    color: var(--sign-white);
    white-space: nowrap;
  }

  .contact {
    position: absolute;
    left: 0; top: 720px;
    width: 597px;
    height: 77px;
    padding: 13px 14px 0 22px;
    font-family: "Tinos", "Times New Roman", serif;
    font-weight: 700;
    font-size: 19px;
    line-height: 24px;
    color: var(--footer-ink);
  }
  .contact__row {
    display: flex;
    justify-content: space-between;
    white-space: nowrap;
  }
  .contact__row--first { margin-right: 6px; }
  .contact__row--second { margin-left: -7px; }
</style>
</head>
<body>
<main class="sign-set">
  <section class="sign sign--sold">
    <div class="sign__panel">
      <h1 class="sign__headline">SOLD</h1>
      <div class="brand">
        <span class="brand__mark"></span>
        <span class="brand__name">BrightPine Real Estate</span>
      </div>
    </div>
    <footer class="contact">
      <p class="contact__row contact__row--first"><span>Contact : Gareth Wimble</span><span>Phone: 0491 650 387</span></p>
      <p class="contact__row contact__row--second"><span>Web: www.bprealestate.com.au</span><span>Email: sales@bprealestate.com.au</span></p>
    </footer>
  </section>

  <section class="sign sign--sale">
    <div class="sign__panel">
      <h1 class="sign__headline">FOR<br>SALE</h1>
      <div class="brand">
        <span class="brand__mark"></span>
        <span class="brand__name">BrightPine Real Estate</span>
      </div>
    </div>
    <footer class="contact">
      <p class="contact__row contact__row--first"><span>Contact : Gareth Wimble</span><span>Phone: 0491 650 387</span></p>
      <p class="contact__row contact__row--second"><span>Web: www.bprealestate.com.au</span><span>Email: sales@bprealestate.com.au</span></p>
    </footer>
  </section>
</main>
</body>
</html>
```